Corwith Lodge website redesign

After 8 years of our current site, we're ready to upgrade our site design. We'd like to generally make it more modern and clean and build it on a CMS like joomla for easier future maintenance.

Our hotel is a family-owned bed and breakfast that competes against much larger hotel chains in Aspen with fancier rooms and larger pricetags. Our hotel is priced moderately and features tasteful, uniquely-design rooms.

We are looking for a website that will showcase the uniqueness of our rooms, the history of the Lodge, and the friendliness of our staff.

Here are some other hotel sites we like:

http://www.brackenfoldhouse.example/

http://www.tollerpeakhaus.example/

http://www.quarrowstay.example/

*********

Scope of Work - I'm looking for a design AND build. The website should be built out in Joomla as part of the final deliverable.
Updates

Current website: http://www.corwithlodge.example/

Explanation of what design + build means:

I am looking for not only the design of the site, but also for the homepage and one subpage to be built out as well. I do NOT need the entire site built - only for those two pages to be built and I will retrofit the remainder of the pages.

Target Market(s)

travellers evaluating hotels in Aspen, Colorado.

Industry/Entity Type

Hotel

Requirements
Must have
• Must, must, must be based on a joomla template. "Rotating" large main image as central position on homepage is a must (see example websites mentioned above).

Nice to have
• We have an existing online reservation system. It would be nice to evaluate placing a "widget" on the homepage that integrates to the online reservation page. Similar to that feature that the Bracken Fold website has at the foot of the main image on their homepage.

```html
<!DOCTYPE html>
<html lang="en">
<head>
<meta charset="utf-8">
<title>Corwith Lodge</title>
<link href="https://fonts.googleapis.com/css2?family=Open+Sans:wght@400;600&family=Noto+Serif:wght@700&display=swap" rel="stylesheet">
<style>
:root{
  --header-dark:#2b2b2b;
  --header-mid:#3a3a3a;
  --nav-top:#5a5a5a;
  --nav-bottom:#3c3c3c;
  --nav-text:#f0f0f0;
  --nav-active:#f39a1e;
  --stage:#8d8d8d;
  --page:#dcdcdc;
  --panel:#f1f1f1;
  --box-border:#d6d6d6;
  --text:#333333;
  --muted:#7a7a7a;
  --link:#2a5aa8;
  --bullet:#e08a1e;
  --footer:#2d2d2d;
  --footer-text:#a0a0a0;
  --badge-green:#5aa02c;
  --button:#2c5fb0;
}
*{box-sizing:border-box;margin:0;padding:0}
html,body{width:1200px;height:1047px;overflow:hidden}
body{position:relative;background:var(--page);font-family:"Open Sans",Verdana,sans-serif;color:var(--text);font-size:12px}
.site-header{position:absolute;left:0;top:0;width:1200px;height:111px;background:linear-gradient(100deg,var(--header-dark) 0%,var(--header-mid) 45%,var(--header-dark) 100%)}
.brand{position:absolute;left:189px;top:26px;color:#e4e4e4;font-size:34px;font-weight:400;letter-spacing:1px}
.tagline{position:absolute;left:189px;top:67px;color:#8a8a8a;font-size:12px;letter-spacing:.5px}
.contact{position:absolute;right:157px;top:66px;display:flex;align-items:center;gap:5px;color:#b5b5b5;font-size:14px}
.contact .sq{width:14px;height:14px;display:inline-block}
.contact .sq.blue{background:#4a78c0}
.main-nav{position:absolute;left:0;top:111px;width:1200px;height:37px;background:linear-gradient(var(--nav-top),var(--nav-bottom));border-top:1px solid #6a6a6a}
.main-nav ul{list-style:none;display:flex;position:absolute;left:159px;top:0;height:37px;border-left:1px solid #2e2e2e}
.main-nav li{padding:0 14px;line-height:37px;color:var(--nav-text);font-size:12.5px;border-right:1px solid #2e2e2e;border-left:1px solid #666}
.main-nav li.active{color:var(--nav-active)}
.main-nav li .caret{display:inline-block;margin-left:7px;border:4px solid transparent;border-top-color:#bbb;vertical-align:-2px}
.stage{position:absolute;left:0;top:148px;width:1200px;height:405px;background:var(--stage)}
.slider-frame{position:absolute;left:159px;top:20px;width:885px;height:341px;background:#aaa;border:1px solid #6c6c6c;border-radius:4px;box-shadow:0 14px 16px -8px rgba(0,0,0,.35)}
.slide{position:absolute;left:8px;top:7px;width:867px;height:322px;background:linear-gradient(90deg,#5a3a28 0%,#8a6446 30%,#7a4e30 55%,#a06c44 80%,#6a4a34 100%)}
.dots{position:absolute;left:565px;top:379px;display:flex;gap:6px}
.dots span{width:12px;height:12px;border-radius:50%;background:#6f6f6f;border:1px solid #9a9a9a}
.dots span.on{background:#e8e8e8}
.content{position:absolute;left:159px;top:553px;width:885px;height:457px;background:var(--panel)}
.box-head{position:absolute;height:41px;background:linear-gradient(#f6f6f6,#dadada);border:1px solid #cfcfcf;border-radius:3px;font-family:"Noto Serif",Georgia,serif;font-weight:700;font-size:17px;color:#555;padding:9px 14px}
.welcome-text{position:absolute;left:26px;top:60px;width:346px;font-size:12.5px;line-height:22.2px;text-align:justify}
.feature-photo{position:absolute;left:387px;top:66px;width:277px;height:183px;background:linear-gradient(160deg,#e8e8ec 0%,#8b5a3c 45%,#5a3a2a 70%,#e6e6ea 100%)}
.caption{position:absolute;left:387px;top:251px;width:277px;text-align:center;color:var(--muted);font-size:12px}
.events{position:absolute;left:26px;top:358px;width:632px;list-style:none}
.events li{position:relative;padding:5px 0 5px 12px;border-bottom:1px dashed #bdbdbd;color:var(--link);font-size:12.5px;line-height:15px;text-align:justify}
.events li::before{content:"";position:absolute;left:2px;top:10px;border:3px solid transparent;border-left:4px solid var(--bullet)}
.side-box{position:absolute;left:694px;width:171px;background:#f4f4f4;border:1px solid var(--box-border);border-radius:3px}
.side-box h3{height:29px;background:linear-gradient(#f6f6f6,#e2e2e2);border-bottom:1px solid var(--box-border);font-weight:400;font-size:12.5px;color:#555;padding:6px 10px;letter-spacing:.3px}
.field{position:absolute;font-size:11.5px;color:#555;letter-spacing:.3px}
.input{position:absolute;height:19px;background:#fff;border:1px solid #aaa}
.select{position:absolute;height:17px;background:#fff;border:1px solid #999;font-size:11px;padding-left:8px;line-height:15px}
.select::after{content:"";position:absolute;right:1px;top:1px;width:13px;height:13px;background:#e4e4e4;border-left:1px solid #bbb}
.submit{position:absolute;left:48px;top:142px;width:78px;height:22px;border-radius:4px;background:linear-gradient(#4a80d0,var(--button));color:#fff;font-size:12.5px;text-align:center;line-height:21px}
.badge{position:absolute;left:13px;top:38px;width:141px;height:117px;background:#fff;border:1px solid var(--badge-green)}
.badge .band{position:absolute;left:0;bottom:0;width:100%;height:19px;background:var(--badge-green)}
.tour-link{position:absolute;left:8px;top:158px;width:155px;text-align:center;color:var(--link);font-size:11px;line-height:13px}
.site-footer{position:absolute;left:0;top:1010px;width:1200px;height:37px;background:var(--footer);color:var(--footer-text);font-size:12.5px;text-align:center;line-height:37px}
</style>
</head>
<body>
<header class="site-header">
  <div class="brand">Corwith Lodge</div>
  <div class="tagline">Located in the heart of downtown Aspen</div>
  <div class="contact">
    <span class="sq blue"></span>
    <svg width="15" height="14" viewBox="0 0 15 14" aria-hidden="true"><rect x="0.5" y="1.5" width="14" height="11" fill="none" stroke="#f0a020" stroke-width="1.5"/><path d="M1 2 L7.5 8 L14 2" fill="none" stroke="#f0a020" stroke-width="1.5"/></svg>
    <svg width="14" height="14" viewBox="0 0 14 14" aria-hidden="true"><rect x="1" y="3" width="12" height="10" rx="1" fill="none" stroke="#b5b5b5" stroke-width="1.4"/><rect x="3" y="1" width="8" height="3" fill="#b5b5b5"/><circle cx="7" cy="8" r="2" fill="#b5b5b5"/></svg>
    <span>970-555-0148</span>
  </div>
</header>

<nav class="main-nav">
  <ul>
    <li class="active">Home</li>
    <li>About The Lodge<span class="caret"></span></li>
    <li>Rooms<span class="caret"></span></li>
    <li>Reservations</li>
    <li>Amenities</li>
    <li>Aspen Information</li>
    <li>webcams</li>
    <li>contactUs</li>
  </ul>
</nav>

<section class="stage">
  <div class="slider-frame">
    <div class="slide" role="img" aria-label="Guest room with carved wooden bed beside the wood-panelled breakfast room"></div>
  </div>
  <div class="dots"><span></span><span class="on"></span><span></span><span></span></div>
</section>

<main class="content">
  <div class="box-head" style="left:13px;top:14px;width:660px">welcome</div>
  <div class="welcome-text">
    <p>Located in the heart of downtown Aspen, the newly renovated Corwith Lodge possesses all the charms of a vintage European Ski Lodge, while offering all of the modern conveniences one would expect with a stay in Aspen.</p>
    <p>A stay at our lodge includes free continental breakfast in our dining room, daily maid service, free wireless internet access, and a fully-equipped conference facility. Guests are also invited to relax in one of our two outdoor Jacuzzis or in our lounge, where a 42-inch plasma TV and fireplace make for a pleasant area to unwind.</p>
  </div>
  <div class="feature-photo" role="img" aria-label="Lodge exterior with timber gables and stone pillars in winter snow"></div>
  <div class="caption">Corwith Lodge Hotel</div>

  <div class="box-head" style="left:13px;top:310px;width:660px">Events</div>
  <ul class="events">
    <li>This winter has really been one for the books. It all started with ...</li>
    <li>Depending on the season, enjoy a huge range of activities from skiing, skating, fly-fishing, hiking, horseback riding...</li>
    <li>*** SPECIAL OFFER *** Stay 3 nights, get the 4th night FREE!</li>
  </ul>

  <aside class="side-box" style="top:14px;height:176px">
    <h3>Availability and Rates</h3>
    <span class="field" style="left:33px;top:45px">Arrival:</span>
    <span class="input" style="left:79px;top:42px;width:86px"></span>
    <span class="field" style="left:12px;top:69px">Departure:</span>
    <span class="input" style="left:79px;top:66px;width:86px"></span>
    <span class="field" style="left:35px;top:94px">Adults:</span>
    <span class="select" style="left:79px;top:92px;width:46px">2</span>
    <span class="field" style="left:23px;top:116px">Children:</span>
    <span class="select" style="left:79px;top:114px;width:46px"></span>
    <span class="submit">submit</span>
  </aside>

  <aside class="side-box" style="top:204px;height:194px">
    <h3>Certificate</h3>
    <div class="badge" role="img" aria-label="Travel review award badge"><div class="band"></div></div>
    <div class="tour-link">Click here for a virtual tour of the lodge!</div>
  </aside>
</main>

<footer class="site-footer">Copyright © 2004-2012 Corwith Lodge. All rights reserved.</footer>
</body>
</html>
```